K7 Electrical Services Ltd Web design

I require a web site for my new electrical contracting company. We are customer service orientated. Offering high value electrical installations, design and maintenance. Focused on custom residential and commercial upgrading. Lighting design and application are paramount in our company's services. Industry leading product use and integration are always on the forefront with our customer client services. As well as energy efficiency.

Target Market(s)

Homebuilders, General Contractors, Property management companies, clients, individuals,

Industry/Entity Type

Electric Company

Coding

Coded - Design and coding required

Number of Pages Required

3 page

Requirements
Must have
• Classic, modern, edgy but not trendy . Appeals to the masse.
• 3 page
• home page
• about page
• gallery page
• ability to contact from the webiste
Nice to have
• open to all types of designs that are relative to the construction industry.
• Black, Grey, metallic ice blue and deep purple colours from the logo.
Should not have
• anything cheesy with cartoon light bulb images.

```html
<!DOCTYPE html>
<html lang="en">
<head>
<meta charset="utf-8">
<title>K7 Electrical Services Ltd</title>
<link rel="stylesheet" href="https://fonts.googleapis.com/css2?family=Barlow:wght@400;500;600;700&display=swap">
<style>
:root{
  --purple:#5c2b8a;
  --purple-deep:#4a1f73;
  --ink:#2c2c2c;
  --text:#4a4a4a;
  --muted:#777;
  --grey-bg:#eeeeee;
  --btn-grey:#6b6b6b;
  --white:#ffffff;
}
*{box-sizing:border-box;margin:0;padding:0}
html,body{width:1200px;height:3448px;overflow:hidden}
body{position:relative;background:var(--white);font-family:"Barlow",Arial,sans-serif;color:var(--text)}
.abs{position:absolute}
svg.abs{display:block}

/* header */
.site-header{left:495px;top:0;width:705px;height:101px;background:rgba(30,30,30,.75)}
.brand{left:50px;top:37px;color:var(--white);font-weight:700;font-size:22px;line-height:26px;white-space:nowrap}
.nav a{position:absolute;top:42px;color:var(--white);font-size:14px;font-weight:700;text-decoration:none;letter-spacing:.5px}
.nav .active::after{content:"";position:absolute;left:0;right:0;bottom:-12px;height:3px;background:var(--purple)}

/* hero */
.hero-title{left:52px;top:165px;color:var(--white);font-weight:700;font-size:47px;line-height:49px;letter-spacing:1px}
.btn{display:flex;align-items:center;justify-content:center;font-weight:700;font-size:15px;letter-spacing:.8px;text-decoration:none}
.btn-light{left:55px;top:398px;width:173px;height:50px;background:var(--white);color:var(--ink)}
.btn-grey{background:var(--btn-grey);color:var(--white)}
.btn-purple{background:var(--purple);color:var(--white)}

/* offer */
.section-title{font-weight:600;font-size:36px;letter-spacing:.5px;color:var(--ink)}
.rule{height:2px;background:#bbb;width:176px}
.offer-item{left:590px;width:570px;height:90px}
.offer-item h3{position:absolute;left:95px;top:0;font-size:23px;font-weight:700;color:var(--ink)}
.offer-item p{position:absolute;left:95px;top:36px;font-size:13.5px;line-height:24px;color:var(--text)}
.offer-item svg{position:absolute;left:0;top:0}

.feature-title{font-weight:700;font-size:35px;line-height:37px;letter-spacing:.5px}
.feature-text{font-size:14px;line-height:24px;color:var(--text)}

.customers-title{left:0;width:1200px;top:2405px;text-align:center;color:var(--purple);font-weight:700;font-size:36px}
.client-row{left:150px;top:2530px;width:900px;display:flex;justify-content:space-between;align-items:center}
.client{font-size:18px;font-weight:600;color:#555;white-space:nowrap}

/* footer */
.footer-brand{left:64px;top:3210px;color:var(--purple);font-weight:700;font-size:24px;line-height:28px;white-space:nowrap}
.footer-about{left:66px;top:3294px;width:330px;font-size:12px;line-height:18px}
.footer-col h4{font-size:13px;color:var(--purple);font-weight:700;letter-spacing:.5px;margin-bottom:26px}
.footer-col li{list-style:none;font-size:13px;font-weight:600;color:var(--ink);line-height:24px;letter-spacing:.4px}
.footer-rule{left:64px;top:3402px;width:1072px;height:1px;background:#ddd}
.copyright{left:0;width:1200px;top:3422px;text-align:center;font-size:12.5px;font-weight:700;color:var(--ink);letter-spacing:.4px}
</style>
</head>
<body>

<div class="abs" style="left:0;top:560px;width:1200px;height:800px;background:var(--grey-bg)"></div>

<svg class="abs" style="left:0;top:0" width="1200" height="700" viewBox="0 0 1200 700" role="img" aria-label="Electrician in a hard hat working at a distribution board">
  <defs>
    <linearGradient id="heroPhoto" x1="0" y1="0" x2="1" y2="1">
      <stop offset="0" stop-color="#3d4c78"/>
      <stop offset=".55" stop-color="#8b93a8"/>
      <stop offset="1" stop-color="#d9dce2"/>
    </linearGradient>
    <clipPath id="heroClip"><polygon points="0,0 1200,0 1200,690 0,612"/></clipPath>
  </defs>
  <g clip-path="url(#heroClip)">
    <rect width="1200" height="700" fill="url(#heroPhoto)"/>
    <polygon points="0,0 495,0 180,700 0,700" fill="var(--purple)" opacity=".92"/>
  </g>
</svg>

<header>
  <div class="abs site-header"></div>
  <div class="abs brand">K7 Electrical Services Ltd</div>
  <nav class="nav">
    <a class="active" href="#" style="left:598px">HOME</a>
    <a href="#" style="left:690px">ABOUT US</a>
    <a href="#" style="left:807px">SERVICES</a>
    <a href="#" style="left:922px">TESTIMONIALS</a>
    <a href="#" style="left:1071px">CONTACT US</a>
  </nav>
</header>

<h1 class="abs hero-title">WE ARE A NEW<br>ELECTRICAL<br>CONTRACTING<br>COMPANY</h1>
<a class="abs btn btn-light" href="#">LEARN MORE</a>

<div class="abs" role="img" aria-label="Smiling electrician with cable coil and tool belt, arms crossed" style="left:138px;top:690px;width:392px;height:685px;background:linear-gradient(180deg,#e9e9e9 0%,#2a2f4a 22%,#1f2440 70%,#6b4a2a 100%)"></div>

<h2 class="abs section-title" style="left:586px;top:778px">WHAT WE OFFER</h2>
<div class="abs rule" style="left:588px;top:836px"></div>

<div class="abs offer-item" style="top:905px">
  <svg width="80" height="80" viewBox="0 0 80 80" fill="none" stroke="var(--purple)" stroke-width="3"><circle cx="40" cy="30" r="14"/><path d="M22 28h36M30 18l4-6h12l4 6"/><path d="M14 76c0-16 12-26 26-26s26 10 26 26"/></svg>
  <h3>ELECTRICAL INSTALLATIONS</h3>
  <p>Sed ut perspiciatis unde omnis iste natus error sit voluptatem accusantium<br>doloremque laudantium, totam rem aperiam</p>
</div>
<div class="abs offer-item" style="top:1030px">
  <svg width="80" height="80" viewBox="0 0 80 80" fill="none" stroke="var(--ink)" stroke-width="3"><rect x="12" y="8" width="44" height="64" rx="3"/><path d="M22 24h24M22 36h24M22 48h16"/><path d="M62 20l8 8-22 30-10 2 2-10z"/></svg>
  <h3>DESIGN</h3>
  <p>Sed ut perspiciatis unde omnis iste natus error sit voluptatem accusantium<br>doloremque laudantium, totam rem aperiam</p>
</div>
<div class="abs offer-item" style="top:1150px">
  <svg width="80" height="80" viewBox="0 0 80 80" fill="none" stroke="var(--ink)" stroke-width="3"><circle cx="26" cy="26" r="16"/><path d="M20 26h12M26 20v12M26 42v30M58 8v64M50 16h16"/></svg>
  <h3>MAINTENANCE</h3>
  <p>Sed ut perspiciatis unde omnis iste natus error sit voluptatem accusantium<br>doloremque laudantium, totam rem aperiam</p>
</div>

<svg class="abs" style="left:0;top:1320px" width="1200" height="560" viewBox="0 0 1200 560">
  <polygon points="0,18 1200,70 1200,560 0,560" fill="var(--white)"/>
</svg>
<svg class="abs" style="left:0;top:1380px" width="1200" height="480" viewBox="0 0 1200 480" role="img" aria-label="Modern two-storey family house at dusk with purple tint">
  <defs><linearGradient id="houseTone" x1="0" y1="0" x2="0" y2="1"><stop offset="0" stop-color="#7a4fb0"/><stop offset="1" stop-color="#4d2380"/></linearGradient></defs>
  <polygon points="650,12 1200,52 1200,480 735,480" fill="url(#houseTone)"/>
  <g fill="none" stroke="var(--white)" stroke-width="7" stroke-linejoin="round">
    <path d="M848 236l94-80 94 80M870 218v138h144V218"/>
    <rect x="892" y="248" width="30" height="30"/><rect x="962" y="248" width="30" height="30"/>
    <path d="M924 356v-46h36v46M848 356h188"/>
  </g>
</svg>

<h2 class="abs feature-title" style="left:50px;top:1483px;color:var(--purple)">CUSTOM<br>RESIDENTIAL</h2>
<div class="abs rule" style="left:52px;top:1582px;width:140px"></div>
<p class="abs feature-text" style="left:52px;top:1608px;width:500px">Sed ut perspiciatis unde omnis iste natus error sit voluptatem accusantium doloremque laudantium, totam rem aperiam, eaque ipsa quae ab illo inventore veritatis et quasi architecto beatae vitae dicta sunt explicabo. Nemo enim ipsam voluptatem quia voluptas sit aspernatur aut odit aut fugit, sed quia consequuntur magni dolores eos qui ratione voluptatem</p>
<a class="abs btn btn-grey" href="#" style="left:55px;top:1755px;width:173px;height:52px">LEARN MORE</a>

<svg class="abs" style="left:0;top:1880px" width="580" height="470" viewBox="0 0 580 470" role="img" aria-label="Dark city office towers seen from below">
  <defs><linearGradient id="cityTone" x1="0" y1="0" x2="1" y2="1"><stop offset="0" stop-color="#4a4a4a"/><stop offset="1" stop-color="#141414"/></linearGradient></defs>
  <polygon points="0,28 568,0 472,466 0,466" fill="url(#cityTone)"/>
  <g fill="none" stroke="var(--white)" stroke-width="7">
    <rect x="186" y="148" width="98" height="198"/>
    <rect x="206" y="172" width="20" height="22"/><rect x="244" y="172" width="20" height="22"/>
    <rect x="206" y="214" width="20" height="22"/><rect x="244" y="214" width="20" height="22"/>
    <rect x="206" y="256" width="20" height="22"/><rect x="244" y="256" width="20" height="22"/>
    <rect x="206" y="298" width="20" height="22"/><rect x="244" y="298" width="20" height="22"/>
    <path d="M166 352h198"/>
  </g>
</svg>
<h2 class="abs feature-title" style="left:610px;top:1958px;color:var(--ink);font-weight:600">COMMERCIAL<br>UPGRADING</h2>
<div class="abs rule" style="left:612px;top:2053px;width:140px"></div>
<p class="abs feature-text" style="left:612px;top:2080px;width:540px">Sed ut perspiciatis unde omnis iste natus error sit voluptatem accusantium doloremque laudantium, totam rem aperiam, eaque ipsa quae ab illo inventore veritatis et quasi architecto beatae vitae dicta sunt explicabo. Nemo enim ipsam voluptatem quia voluptas sit aspernatur aut odit aut fugit, sed quia consequuntur magni dolores eos qui ratione voluptatem</p>
<a class="abs btn btn-purple" href="#" style="left:612px;top:2247px;width:172px;height:52px">LEARN MORE</a>

<h2 class="abs customers-title">OUR HAPPY CUSTOMERS</h2>
<div class="abs rule" style="left:510px;top:2470px;width:180px"></div>
<div class="abs client-row">
  <span class="client">Quenby Lettings</span>
  <span class="client">Ashvale Borough</span>
  <span class="client">Thornwick &amp; Pell</span>
  <span class="client">Calderbrook Structures</span>
  <span class="client">Wexmoor Council</span>
</div>

<svg class="abs" style="left:0;top:2615px" width="1200" height="575" viewBox="0 0 1200 575">
  <polygon points="0,45 1200,0 1200,575 0,575" fill="var(--grey-bg)"/>
</svg>
<div class="abs" role="img" aria-label="Video still: two electricians standing beside a white work van" style="left:230px;top:2702px;width:738px;height:373px;background:linear-gradient(135deg,#2b3550 0%,#6f8fb5 45%,#d7dde6 75%,#3aa0c8 100%);box-shadow:0 10px 30px rgba(0,0,0,.25)"></div>
<svg class="abs" style="left:559px;top:2852px" width="80" height="80" viewBox="0 0 80 80"><circle cx="40" cy="40" r="36" fill="rgba(0,0,0,.35)" stroke="var(--white)" stroke-width="4"/><path d="M32 25l24 15-24 15z" fill="var(--white)"/></svg>

<footer>
  <div class="abs footer-brand">K7 Electrical Services Ltd</div>
  <p class="abs footer-about">Sed ut perspiciatis unde omnis iste natus error sit voluptatem accusantium doloremque laudantium, totam rem aperiam, eaque ipsa quae ab illo inventore veritatis et quasi architecto beatae vitae dicta sunt explicabo.</p>
  <div class="abs footer-col" style="left:453px;top:3192px">
    <h4>QUICK LINKS</h4>
    <ul><li>HOME</li><li>ABOUT US</li><li>SERVICES</li><li>TESTIMONIALS</li><li>CONTACT US</li></ul>
  </div>
  <div class="abs footer-col" style="left:665px;top:3192px">
    <h4>OTHER LINKS</h4>
    <ul><li>TERMS OF USE</li><li>PRIVACY POLICY</li><li>HELP</li><li>DISCLAIMER</li></ul>
  </div>
  <div class="abs footer-col" style="left:849px;top:3192px">
    <h4>CONNECT WITH US</h4>
  </div>
  <svg class="abs" style="left:851px;top:3237px" width="110" height="30" viewBox="0 0 110 30" fill="none" stroke="#999" stroke-width="1.5">
    <circle cx="15" cy="15" r="13"/><circle cx="50" cy="15" r="13"/><circle cx="85" cy="15" r="13"/>
  </svg>
  <div class="abs footer-rule"></div>
  <div class="abs copyright">© 2018 COMPANY NAME &nbsp;|&nbsp; ALL RIGHTS RESERVED</div>
</footer>

</body>
</html>
```